Professional Label needed for Meadowpaw Snack Co

I make 100% organic dog treats. Wheat and gluten free.

I will be packaging them in a window kraft bag. I need a nicely designed label to place on each bag. The name of my company is The Meadowpaw Snack Company. All ingredients are organic and no preservatives are used. They are a healthy alternative to "assembly line" treats made by large companies.

Target Market(s)

Dog Owners

Industry/Entity Type

Pet

Font styles to use
Serif

Colors
00a990

Requirements
Must have
• can use a dog paw - see attached files. Dog themed, 100%
• Organic Dog Treats.
• No preservatives, nothing artificial, no corn, wheat or soy, made in Texas, USA with 100% organic ingredients. Non GMO
• Must have "dog treat" somewhere.
• "The Meadowpaw Snack Co." font size needs to be bigger than anything else.
Nice to have
• I like teal and brown
• I'm open to anything really as long as its dog themed

```html
<!DOCTYPE html>
<html lang="en">
<head>
<meta charset="utf-8">
<title>The Meadowpaw Snack Company – Treat Bag Label</title>
<link href="https://fonts.googleapis.com/css2?family=Noto+Serif:wght@400;700&family=Leckerli+One&display=swap" rel="stylesheet">
<style>
  :root {
    --page-bg: #e9e4dc;
    --label-bg: #ffffff;
    --label-edge: #3a3a3a;
    --ink: #1e1c1d;
    --leaf-green: #2f7d3f;
    --art-top: #b3a596;
    --art-bottom: #8fc9bb;
  }
  * { box-sizing: border-box; margin: 0; padding: 0; }
  html, body {
    width: 1200px;
    height: 1200px;
    overflow: hidden;
    background: var(--page-bg);
  }
  .label {
    position: absolute;
    left: 50px;
    top: 50px;
    width: 1100px;
    height: 1100px;
    background: var(--label-bg);
    border: 2px solid var(--label-edge);
    font-family: "Noto Serif", Georgia, serif;
    color: var(--ink);
  }
  .stitch-border {
    position: absolute;
    inset: 20px;
    border: 2px dashed var(--ink);
  }
  .company-name {
    position: absolute;
    top: 44px;
    left: 0;
    width: 100%;
    text-align: center;
    font-size: 52px;
    font-weight: 700;
    white-space: nowrap;
    line-height: 1.2;
  }
  .company-name .accent { color: var(--leaf-green); }
  .mascot-art {
    position: absolute;
    left: 310px;
    top: 170px;
    width: 490px;
    height: 430px;
    border-radius: 24px;
    background: linear-gradient(180deg, var(--art-top) 0%, var(--art-bottom) 100%);
  }
  .product-name {
    position: absolute;
    top: 600px;
    left: 0;
    width: 100%;
    text-align: center;
    font-family: "Leckerli One", cursive;
    font-size: 190px;
    line-height: 1;
    white-space: nowrap;
    color: var(--ink);
  }
  .product-tag {
    position: absolute;
    top: 780px;
    right: 58px;
    font-size: 60px;
    font-weight: 700;
    color: var(--leaf-green);
    line-height: 1;
  }
  .product-claims {
    position: absolute;
    top: 928px;
    left: 0;
    width: 100%;
    text-align: center;
    font-size: 28px;
    font-weight: 700;
    line-height: 34px;
  }
  .product-claims .non-gmo { font-weight: 400; }
</style>
</head>
<body>
  <main class="label">
    <div class="stitch-border"></div>
    <h1 class="company-name"><span class="accent">The Meadowpaw</span> Snack Company</h1>
    <div class="mascot-art" role="img" aria-label="Illustration of a cartoon dog mascot wearing a beret and a teal bandana"></div>
    <p class="product-name">Dog Treats</p>
    <p class="product-tag">Organic</p>
    <p class="product-claims">
      No preservatives, nothing artificial, no corn, wheat or soy.<br>
      Made in Texas, USA with 100% organic ingredients.<br>
      <span class="non-gmo">Non GMO</span>
    </p>
  </main>
</body>
</html>
```